依頼詳細
化粧水 パッケージデザイン
箱無し
シンプルかつ高級感のあるデザイン
ミレニアム世代、50代、60代をメインとし販売
自社ハーブ畑で撮影した写真
(カモミール)を使用していただき、こちら写真をメインとし
ロゴ、ネーミングの配置
全体的なイメージのデザインを依頼いたします。

記載項目
・大きさ:縦108mm×140mm
・化粧品表示のルールで、文字の大きさは7ポイント以上、 ・プラマークの大きさは高さを6mm以上にしてください。 ・円柱の容器に1枚のシールをぐるっと巻きつけて貼る形になります。

ラミネート加工
カラーはパール入りデザイン希望

金文字で、ブランド名
『VELMIRAE』記載希望
希望イメージ
シンプル 複雑
単色 カラフル
暗い 明るい
日常 高級
遊び心 厳粛
未来的 伝統的
女性的 男性的
希望する色
赤系、水色系、黄・オレンジ系、追加、ホワイトパール系のカラー
■ 選んだ理由

自社のハーブ素材を生かし、+アルファの工夫があり好感度を持てた。シンプルな上に必要な情報が記載されて良い。

■ 提案者全員のお礼・コメント

多くのご提案、誠にありがとうございました。また、自社製品を作成していく上でお力添えをいただく事もあると思います、何卒よろしくお願い申し上げます。

```html
<!DOCTYPE html>
<html lang="en">
<head>
<meta charset="utf-8">
<title>VELMIRAE Herbal Mist Spray – Label</title>
<link rel="stylesheet" href="https://fonts.googleapis.com/css2?family=Cinzel:wght@500;600&family=Cormorant+Garamond:ital,wght@0,500;1,500&family=Lato:wght@400&display=swap">
<style>
  :root {
    --page: #ffffff;
    --ink: #1a1a1a;
    --gold: #b8914a;
    --gold-light: #dcc38e;
    --gold-deep: #94712f;
    --pearl: #fbf9f4;
    --meadow-light: #e6ead8;
    --meadow: #b7c18f;
    --meadow-deep: #7d8a52;
    --petal: #fdfdfa;
  }
  html, body {
    margin: 0;
    padding: 0;
    width: 846px;
    height: 1200px;
    overflow: hidden;
    background: var(--page);
  }
  .canvas {
    position: relative;
    width: 846px;
    height: 1200px;
    background: var(--page);
  }
  .title-block {
    position: absolute;
    left: 96px;
    top: 108px;
    width: 200px;
    text-align: center;
    color: var(--ink);
  }
  .title-block__brand {
    font-family: "Cinzel", serif;
    font-weight: 500;
    font-size: 27px;
    letter-spacing: 0.5px;
    line-height: 1;
    margin: 0;
  }
  .title-block__product {
    font-family: "Lato", sans-serif;
    font-size: 11px;
    margin: 8px 0 0;
  }
  .label {
    position: absolute;
    left: 302px;
    top: 423px;
    width: 400px;
    height: 319px;
    background: var(--pearl);
    overflow: hidden;
    box-shadow: 0 0 0 1px #eeeae0;
  }
  .label__photo {
    position: absolute;
    left: 0;
    width: 100%;
  }
  .label__photo--top {
    top: 0;
    height: 120px;
    background:
      radial-gradient(ellipse 60px 40px at 18% 45%, var(--petal) 0%, rgba(255,255,255,0) 80%),
      radial-gradient(ellipse 70px 45px at 62% 35%, var(--petal) 0%, rgba(255,255,255,0) 80%),
      radial-gradient(ellipse 50px 35px at 88% 60%, var(--petal) 0%, rgba(255,255,255,0) 80%),
      linear-gradient(180deg, var(--meadow) 0%, var(--meadow-light) 70%, var(--pearl) 100%);
  }
  .label__photo--bottom {
    bottom: 0;
    height: 105px;
    background:
      radial-gradient(ellipse 60px 40px at 25% 60%, var(--petal) 0%, rgba(255,255,255,0) 80%),
      radial-gradient(ellipse 70px 40px at 70% 55%, var(--petal) 0%, rgba(255,255,255,0) 80%),
      linear-gradient(0deg, var(--meadow-deep) 0%, var(--meadow) 40%, var(--meadow-light) 80%, var(--pearl) 100%);
  }
  .label__band {
    position: absolute;
    left: 0;
    top: 112px;
    width: 100%;
    height: 108px;
    background: linear-gradient(180deg, rgba(251,249,244,0.9), var(--pearl) 20%, var(--pearl) 80%, rgba(251,249,244,0.9));
  }
  .label__rule {
    position: absolute;
    left: 0;
    width: 100%;
  }
  .label__rule--top { top: 106px; }
  .label__rule--bottom { top: 218px; }
  .label__crest {
    position: absolute;
    left: 178px;
    top: 78px;
    width: 44px;
    height: 44px;
  }
  .label__name {
    position: absolute;
    left: 0;
    top: 138px;
    width: 100%;
    text-align: center;
    font-family: "Cinzel", serif;
    font-weight: 600;
    font-size: 30px;
    letter-spacing: 1px;
    line-height: 1;
    color: var(--gold);
    margin: 0;
  }
  .label__product {
    position: absolute;
    left: 0;
    top: 176px;
    width: 100%;
    text-align: center;
    font-family: "Cormorant Garamond", serif;
    font-style: italic;
    font-weight: 500;
    font-size: 14px;
    color: var(--gold-deep);
    margin: 0;
  }
  .label__note {
    position: absolute;
    left: 44px;
    top: 204px;
    font-family: "Lato", sans-serif;
    font-size: 7px;
    color: var(--gold-deep);
    margin: 0;
  }
  .label__seal {
    position: absolute;
    left: 334px;
    top: 236px;
    width: 30px;
    height: 12px;
    background: var(--gold-light);
    border-radius: 2px;
  }
  .label__recycle {
    position: absolute;
    left: 364px;
    top: 268px;
    width: 20px;
    height: 22px;
    border: 2px solid #ffffff;
    border-radius: 3px;
    box-sizing: border-box;
  }
</style>
</head>
<body>
<main class="canvas">
  <header class="title-block">
    <h1 class="title-block__brand">VELMIRAE</h1>
    <p class="title-block__product">Herbal Mist Spray</p>
  </header>

  <section class="label" aria-label="Wrap-around bottle label">
    <div class="label__photo label__photo--top" role="img" aria-label="Photograph of white chamomile flowers in the herb field"></div>
    <div class="label__photo label__photo--bottom" role="img" aria-label="Photograph of chamomile flowers and green foliage"></div>
    <div class="label__band"></div>

    <svg class="label__rule label__rule--top" width="400" height="8" viewBox="0 0 400 8">
      <line x1="0" y1="2" x2="400" y2="2" stroke="#dcc38e" stroke-width="1"/>
      <line x1="0" y1="6" x2="400" y2="6" stroke="#b8914a" stroke-width="1.5"/>
    </svg>
    <svg class="label__rule label__rule--bottom" width="400" height="8" viewBox="0 0 400 8">
      <line x1="0" y1="2" x2="400" y2="2" stroke="#b8914a" stroke-width="1.5"/>
      <line x1="0" y1="6" x2="400" y2="6" stroke="#dcc38e" stroke-width="1"/>
    </svg>

    <svg class="label__crest" viewBox="0 0 44 44" aria-hidden="true">
      <circle cx="22" cy="22" r="20" fill="#fbf9f4" stroke="#b8914a" stroke-width="1.5"/>
    </svg>

    <h2 class="label__name">VELMIRAE</h2>
    <p class="label__product">Herbal Mist Spray</p>
    <p class="label__note">Botanical Lotion</p>

    <div class="label__seal" aria-hidden="true"></div>
    <div class="label__recycle" aria-hidden="true"></div>
  </section>
</main>
</body>
</html>
```